Landing Page / Waitlist

I would like a landing page for people to sign up for a waiting list. The text on the page should include (but is not limited to):
1) Main point: The accounting system you'll love
2) Secondary points:
a. Ruthlessly efficient
b. Quietly intelligent
c. Driven by AI
I've attached a file of our logo

The design should be simple, clean, and innovative - this is an ai company

```html
<!DOCTYPE html>
<html lang="en">
<head>
<meta charset="utf-8">
<title>LedgerBloom — Join the Waiting List</title>
<link href="https://fonts.googleapis.com/css2?family=Poppins:wght@300;400;500;600;700&display=swap" rel="stylesheet">
<style>
  :root {
    --bg-deep: #03080f;
    --bg-mid: #0a1e33;
    --bg-glow: #12395e;
    --text: #ffffff;
    --text-soft: #e6edf5;
    --accent: #1a9bff;
    --accent-light: #27c0ff;
    --accent-dark: #0a7df0;
    --line: rgba(255, 255, 255, 0.55);
    --hex-line: rgba(255, 255, 255, 0.45);
    --footer-bg: rgba(12, 28, 44, 0.78);
  }
  * { box-sizing: border-box; margin: 0; padding: 0; }
  html, body {
    width: 1200px;
    height: 668px;
    overflow: hidden;
    background: var(--bg-deep);
    font-family: "Poppins", sans-serif;
    color: var(--text);
  }
  .page {
    position: relative;
    width: 1200px;
    height: 668px;
    overflow: hidden;
  }
  .hero-backdrop {
    position: absolute;
    inset: 0;
    background:
      radial-gradient(ellipse 260px 120px at 440px 400px, rgba(70, 140, 200, 0.35), transparent 70%),
      radial-gradient(ellipse 420px 360px at 1020px 300px, rgba(40, 90, 140, 0.45), transparent 70%),
      radial-gradient(ellipse 500px 300px at 200px 200px, rgba(20, 60, 100, 0.35), transparent 70%),
      linear-gradient(180deg, var(--bg-deep) 0%, var(--bg-mid) 60%, var(--bg-deep) 100%);
  }
  .brand {
    position: absolute;
    top: 78px;
    left: 0;
    width: 100%;
    text-align: center;
    font-weight: 600;
    font-size: 31px;
    letter-spacing: -0.5px;
    color: var(--text);
  }
  .headline {
    position: absolute;
    top: 204px;
    left: 0;
    width: 100%;
    text-align: center;
    line-height: 1.1;
  }
  .headline-strong {
    display: block;
    font-weight: 600;
    font-size: 51px;
  }
  .headline-light {
    display: block;
    font-weight: 300;
    font-size: 48px;
  }
  .waitlist-form {
    position: absolute;
    top: 345px;
    left: 212px;
    width: 777px;
    height: 46px;
  }
  .email-field {
    position: absolute;
    left: 0;
    top: 0;
    width: 599px;
    height: 46px;
    border: 1px solid var(--line);
    border-radius: 23px;
    background: transparent;
    color: var(--text);
    font-family: "Poppins", sans-serif;
    font-weight: 500;
    font-size: 14px;
    padding-left: 24px;
    outline: none;
  }
  .email-field::placeholder { color: var(--text); opacity: 1; }
  .join-button {
    position: absolute;
    left: 606px;
    top: 0;
    width: 171px;
    height: 46px;
    border: none;
    border-radius: 23px;
    background: linear-gradient(90deg, var(--accent-light), var(--accent-dark));
    color: var(--text);
    font-family: "Poppins", sans-serif;
    font-weight: 600;
    font-size: 14px;
  }
  .features {
    position: absolute;
    top: 473px;
    left: 0;
    width: 100%;
    height: 77px;
  }
  .feature {
    position: absolute;
    top: 0;
    height: 77px;
    display: flex;
    align-items: center;
    gap: 20px;
  }
  .feature-icon { width: 67px; height: 77px; flex: none; }
  .feature-label {
    font-weight: 500;
    font-size: 19px;
    letter-spacing: 0.2px;
    text-transform: uppercase;
    color: var(--text-soft);
  }
  .feature-efficient { left: 147px; }
  .feature-ai { left: 505px; }
  .feature-intelligent { left: 771px; }
  .site-footer {
    position: absolute;
    left: 0;
    bottom: 0;
    width: 100%;
    height: 84px;
    background: var(--footer-bg);
    display: flex;
    align-items: center;
    justify-content: center;
    font-size: 14px;
    color: var(--text-soft);
  }
  .footer-divider { margin: 0 12px; }
</style>
</head>
<body>
<main class="page">
  <div class="hero-backdrop" role="img" aria-label="Dark blue photo of an open hand with a glowing network of connected data points"></div>

  <div class="brand">LedgerBloom</div>

  <h1 class="headline">
    <span class="headline-strong">The accounting system</span>
    <span class="headline-light">you'll love</span>
  </h1>

  <form class="waitlist-form">
    <input class="email-field" type="email" placeholder="Email Address" aria-label="Email Address">
    <button class="join-button" type="button">Join Waiting List</button>
  </form>

  <section class="features">
    <div class="feature feature-efficient">
      <svg class="feature-icon" viewBox="0 0 67 77" aria-hidden="true">
        <polygon points="33.5,1 66,19.75 66,57.25 33.5,76 1,57.25 1,19.75" fill="none" stroke="var(--hex-line)" stroke-width="1"/>
        <polyline points="19,48 28,38 35,44 47,30" fill="none" stroke="var(--accent)" stroke-width="4" stroke-linecap="round" stroke-linejoin="round"/>
        <polyline points="39,29 48,29 48,38" fill="none" stroke="var(--accent)" stroke-width="4" stroke-linecap="round" stroke-linejoin="round"/>
      </svg>
      <span class="feature-label">Ruthlessly Efficient</span>
    </div>
    <div class="feature feature-ai">
      <svg class="feature-icon" viewBox="0 0 67 77" aria-hidden="true">
        <polygon points="33.5,1 66,19.75 66,57.25 33.5,76 1,57.25 1,19.75" fill="none" stroke="var(--hex-line)" stroke-width="1"/>
        <rect x="22" y="27" width="23" height="23" rx="3" fill="var(--accent)"/>
        <g stroke="var(--accent)" stroke-width="2.5" stroke-linecap="round">
          <line x1="28" y1="22" x2="28" y2="27"/><line x1="39" y1="22" x2="39" y2="27"/>
          <line x1="28" y1="50" x2="28" y2="55"/><line x1="39" y1="50" x2="39" y2="55"/>
          <line x1="17" y1="33" x2="22" y2="33"/><line x1="17" y1="44" x2="22" y2="44"/>
          <line x1="45" y1="33" x2="50" y2="33"/><line x1="45" y1="44" x2="50" y2="44"/>
        </g>
      </svg>
      <span class="feature-label">Driven by AI</span>
    </div>
    <div class="feature feature-intelligent">
      <svg class="feature-icon" viewBox="0 0 67 77" aria-hidden="true">
        <polygon points="33.5,1 66,19.75 66,57.25 33.5,76 1,57.25 1,19.75" fill="none" stroke="var(--hex-line)" stroke-width="1"/>
        <g stroke="var(--accent)" stroke-width="2.5">
          <line x1="24" y1="30" x2="40" y2="26"/><line x1="24" y1="30" x2="30" y2="44"/>
          <line x1="40" y1="26" x2="44" y2="42"/><line x1="30" y1="44" x2="44" y2="42"/>
          <line x1="30" y1="44" x2="36" y2="52"/>
        </g>
        <g fill="var(--accent)">
          <circle cx="24" cy="30" r="4.5"/><circle cx="40" cy="26" r="4.5"/>
          <circle cx="30" cy="44" r="4.5"/><circle cx="44" cy="42" r="4.5"/>
          <circle cx="36" cy="52" r="3.5"/>
        </g>
      </svg>
      <span class="feature-label">Quietly Intelligent</span>
    </div>
  </section>

  <footer class="site-footer">
    <span>Copyright© 2025 LEDGERBLOOM</span>
    <span class="footer-divider">/</span>
    <span>All Rights Reserved</span>
  </footer>
</main>
</body>
</html>
```